Web Design Project - brivocell

I'm building an agency for marketing solutions but also medical education and patients education for pharmaceutical companies, medical societies and patient advocacy groups. We want to be perceived as the most innovative in the market. We work through design thinking solutions for campaigns and services.
I love some websites based on Swiss style design like www.plumvane.example
We are a small group of designers, physicians and creatives working together to deliver the best experiences in our market.
We decided to also use pixel forum expecting that we maybe found a great idea we didn't thought about yet.

I'm extending it for more 2 weeks

Reason: I need the best design you can. Only PSD. No code needed. Love Swiss style, like tessera 5 and plumvane.example I'm extending the deadline until get something great. Willing to extend as much as needed.

Target Market(s)

Pharmaceutical companies, physicians, medical societies, patients advocacy groups

Industry/Entity Type

Pharmaceutical

Font styles to use
Other font styles liked:
• Helvetia family

Colors

Designer to choose colors to be used in the design.

Requirements
Must have
• Must be innovative like www.plumvane.example
Nice to have
• Cool menus
Should not have
• Not to appear too much Comercial. We like to be a boutique in this market. Craftsmen working with less clients at time but delivering precious stones.

```html
<!DOCTYPE html>
<html lang="en">
<head>
<meta charset="utf-8">
<title>brivocell</title>
<link rel="stylesheet" href="https://fonts.googleapis.com/css2?family=Arimo:wght@400;700&family=Open+Sans:wght@300;400;600&display=swap">
<style>
:root{
  --cyan:#1ab3e6;
  --blue:#0e9acb;
  --orange:#f07d1e;
  --orange-soft:rgba(244,126,28,.9);
  --ink:#222;
  --grey:#555;
  --band:rgba(240,240,240,.92);
  --white:#fff;
}
*{margin:0;padding:0;box-sizing:border-box}
html,body{width:957px;height:1200px;overflow:hidden;background:var(--white)}
body{position:relative;font-family:"Arimo",Arial,sans-serif;color:var(--ink)}
.site-header{position:absolute;left:0;top:0;width:957px;height:54px;border-bottom:3px solid var(--orange)}
.brand{position:absolute;left:78px;top:10px;font-size:30px;font-weight:400;color:var(--cyan);letter-spacing:.5px}
.main-nav{position:absolute;top:10px;left:0;width:957px;height:40px}
.main-nav a{position:absolute;top:0;display:block;width:40px;height:36px;margin-left:-20px}
.main-nav svg{width:40px;height:36px;fill:none;stroke:#222;stroke-width:2;stroke-linejoin:round;stroke-linecap:round}
.nav-marker{position:absolute;left:502px;top:46px;width:0;height:0;border-left:6px solid transparent;border-right:6px solid transparent;border-bottom:6px solid var(--orange)}
.hero{position:absolute;left:0;top:57px;width:957px;height:345px;background:linear-gradient(100deg,#cfd4d6 0%,#7b8c92 25%,#3a3735 45%,#6b5444 62%,#c59478 78%,#e9d5c8 100%)}
.hero-card{position:absolute;left:79px;top:175px;width:396px;height:118px;background:var(--orange-soft);padding:9px 18px 0 18px;color:var(--white)}
.hero-card h1{font-size:23px;font-weight:700;letter-spacing:.8px;line-height:26px}
.hero-card p{margin-top:6px;font-size:10px;line-height:14.5px;color:#1b1b1b;width:355px}
.btn{position:absolute;left:20px;top:90px;width:73px;height:19px;background:var(--blue);border-radius:3px;color:var(--white);font-size:10px;line-height:19px;text-align:center}
.welcome{position:absolute;left:79px;top:442px;width:371px;height:272px;background:var(--blue);color:var(--white);padding:10px 14px 0 15px}
.welcome h2{font-size:28px;font-weight:400;line-height:34px}
.welcome h2 strong{font-size:37px;color:#1f2a30;font-weight:400}
.welcome p{margin-top:4px;padding-left:4px;font-family:"Open Sans",Arial,sans-serif;font-weight:300;font-size:21px;line-height:33px;letter-spacing:1.3px}
.welcome p b{font-weight:600}
.welcome-photo{position:absolute;left:450px;top:442px;width:429px;height:272px;background:linear-gradient(120deg,#6f8fae 0%,#c6d3dd 40%,#eef1f3 70%,#d2d8dc 100%)}
.edu-photo{position:absolute;left:80px;top:765px;width:254px;height:161px;background:linear-gradient(90deg,#dfe4e8 0%,#f3f1ee 50%,#c9b8a6 100%)}
.edu{position:absolute;left:375px;top:757px;width:520px}
.edu h2{font-family:"Open Sans",Arial,sans-serif;font-weight:300;font-size:40px;color:var(--blue);letter-spacing:2px;line-height:50px}
.edu p{margin-top:3px;font-family:"Open Sans",Arial,sans-serif;font-weight:300;font-size:20.5px;line-height:29px;color:var(--grey);letter-spacing:1.4px}
.service{position:absolute;top:976px;width:242px;height:170px}
.service .photo{width:242px;height:170px}
.service h3{position:absolute;left:0;bottom:0;width:242px;height:34px;background:var(--band);font-size:19px;font-weight:700;line-height:34px;text-align:center;letter-spacing:.6px;color:#111}
.pharma{left:80px}.pharma .photo{background:linear-gradient(135deg,#c9a24a 0%,#efe9e2 45%,#b8322a 70%,#f2ece6 100%)}
.marketing{left:360px}.marketing .photo{background:linear-gradient(135deg,#e8e9ea 0%,#bdbfc2 50%,#f5f5f5 100%)}
.patients{left:638px}.patients .photo{background:linear-gradient(135deg,#9a8575 0%,#d9dde3 50%,#f3f4f7 100%)}
.site-footer{position:absolute;left:0;top:1169px;width:957px;height:31px;background:var(--cyan);color:var(--white);font-size:12px;line-height:31px;text-align:center}
</style>
</head>
<body>
<header class="site-header">
  <div class="brand">brivocell</div>
  <nav class="main-nav">
    <a style="left:508px" aria-label="Home"><svg viewBox="0 0 40 36"><path d="M4 18 20 4l16 14M9 14v19h9V22h4v11h9V14"/></svg></a>
    <a style="left:599px" aria-label="Services"><svg viewBox="0 0 40 36"><rect x="4" y="9" width="32" height="24" rx="3"/><path d="M15 9V5h10v4M20 15v12M14 21h12"/></svg></a>
    <a style="left:686px" aria-label="Ideas"><svg viewBox="0 0 40 36"><path d="M14 18a6 6 0 1 1 12 0c0 4-3 5-3 9h-6c0-4-3-5-3-9zM17 30h6M18 33h4M17 18l3 4 3-4M6 16h3M31 16h3M10 7l2 2M30 7l-2 2M20 2v3"/></svg></a>
    <a style="left:766px" aria-label="Products"><svg viewBox="0 0 40 36"><rect x="14" y="2" width="12" height="5"/><path d="M13 7h14v27H13zM20 15v10M15 20h10"/></svg></a>
    <a style="left:858px" aria-label="Contact"><svg viewBox="0 0 40 36"><rect x="5" y="10" width="30" height="20" rx="2"/><circle cx="14" cy="18" r="3"/><path d="M9 26c1-4 9-4 10 0M22 26h9"/><circle cx="27" cy="18" r="3"/></svg></a>
  </nav>
  <span class="nav-marker"></span>
</header>

<section class="hero" role="img" aria-label="Smiling young researcher beside a microscope in a laboratory">
  <div class="hero-card">
    <h1>LOREM IPSUM DOLOR:</h1>
    <p>Lorem ipsum dolor sit amet, consectetur adipiscing elit, sed do dolor in reprehenderit in voluptate velit esse cillum dolore eu fugiat nulla pariatur.</p>
    <a class="btn">Read More</a>
  </div>
</section>

<section class="welcome">
  <h2>welcome to <strong>brivocell</strong></h2>
  <p>simply dummy text of the print-ing and typesetting industry. <b>Lorem Ipsum</b> has been the in-dustry's standard dummy text ever since the 1500s, when an unknown printer took a galley.</p>
</section>
<div class="welcome-photo" role="img" aria-label="Lab technician in a white coat and hair net handling a sample"></div>

<div class="edu-photo" role="img" aria-label="Group of smiling doctors and nurses"></div>
<section class="edu">
  <h2>Medical education</h2>
  <p>simply dummy text of the printing and typeset-ting industry. Lorem Ipsum has been the in-dustry's standard dummy text ever since the 1500s, when an unknown a galley.</p>
</section>

<article class="service pharma"><div class="photo" role="img" aria-label="Assorted pills and capsules"></div><h3>Pharmaceutical</h3></article>
<article class="service marketing"><div class="photo" role="img" aria-label="Team reviewing charts on a table"></div><h3>Marketing Solutions</h3></article>
<article class="service patients"><div class="photo" role="img" aria-label="Person working on a laptop"></div><h3>Patients Education</h3></article>

<footer class="site-footer">© 2014 brivocell. All Rights Reserved I Privacy Policy</footer>
</body>
</html>
```